Locksmith SmartPhone Web Design Project

I am a locksmith and focus on customers that use their smart phones to find me. I have a static web page that I created myself but it is horrible. See for yourself at www.brevalkeyworks.com.au

I want a cross-platform static site that simply shows the information and with the ability to change minor items like pricing. I want it to be compelling in its look and feel (not overwhelming) but simple. It must have a; click to call button; the ability to install a hit counter from pagetallyo.com; payment information just like the current graphic of card/cash/quidlo (orla/brixalonte only).

This will be hosted on my own server.
Updates

Hello Designers,

I have updated the brief in the must have and nice to have fields.

Thank you all,

Tom.

Hello to all Designers,

There is about 9 days left before the deadline. The overall level of competition is extremely high and I would like to thank all the designers who have submitted so far, 27 submissions in total so far. Excellent work.

If you have submitted already and wish to provide new designs, I am keen to see them. 

Hi guys, time is almost up. Please submit any new designs that you may have. The quality has been excellent so far.

Tom.

Target Market(s)

People who are locked out of their house/shop/office etc.

Industry/Entity Type

Locksmith

Requirements
Must have
• click to call button
hit counter from pagetallyo
payment graphic card/cash/quidlo (orla/brixalonte only)
cross platform compatibility smartphone/phablet
Single column page preferable, can have two columns.
Nice to have
• When the page loads regardless of the mobile device, all info should be presented. In other words no vertical or horizontal scroll bars.
Should not have
• hidden code, advertising, credits etc

```html
<!DOCTYPE html>
<html lang="en">
<head>
<meta charset="utf-8">
<title>Breval Keyworks</title>
<link rel="stylesheet" href="https://fonts.googleapis.com/css2?family=Russo+One&family=Orbitron:wght@500;700&display=swap">
<style>
  :root {
    --bg: #3b3b3b;
    --bg-dark: #232323;
    --header: #262626;
    --title-blue: #1f86e8;
    --title-edge: #0b2f5a;
    --text: #ffffff;
    --offer-blue: #2a8ff2;
    --button-top: #2f86f0;
    --button-bottom: #0b3fa8;
    --card-face: #f4f4f4;
    --card-ink: #1d2a44;
    --keys-fill: #8a8680;
    --stopwatch: #8e1c1c;
    --cash: #7f8e6a;
  }
  * { margin: 0; padding: 0; box-sizing: border-box; }
  html, body { width: 800px; height: 1200px; overflow: hidden; }
  body {
    background: radial-gradient(ellipse at 50% 40%, #444 0%, var(--bg) 55%, #2e2e2e 100%);
    color: var(--text);
    font-family: "Orbitron", sans-serif;
    position: relative;
  }
  .site-header {
    position: absolute; top: 0; left: 0; width: 800px; height: 135px;
    background: var(--header);
    text-align: center;
  }
  .brand-name {
    font-family: "Russo One", sans-serif;
    font-size: 58px; letter-spacing: 3px;
    color: var(--title-blue);
    -webkit-text-stroke: 1.5px var(--title-edge);
    padding-top: 14px; line-height: 1;
    text-transform: uppercase;
  }
  .phone {
    font-size: 32px; font-weight: 500; letter-spacing: 2px;
    margin-top: 14px;
  }
  .keys {
    position: absolute; top: 160px; left: 112px; width: 588px; height: 230px;
    background: linear-gradient(180deg, #5a5652 0%, var(--keys-fill) 45%, #6d6a66 100%);
    border-radius: 20px;
  }
  .question {
    position: absolute; top: 412px; width: 800px; text-align: center;
    font-size: 29px; font-weight: 500;
  }
  .offer-band {
    position: absolute; top: 458px; left: 22px; width: 756px; height: 70px;
    background: linear-gradient(90deg, transparent 0%, var(--bg-dark) 12%, var(--bg-dark) 88%, transparent 100%);
    text-align: center; line-height: 70px;
    color: var(--offer-blue); font-size: 30px; font-weight: 500; letter-spacing: 1px;
    text-transform: uppercase;
  }
  .service-badge {
    position: absolute; top: 555px; left: 310px; width: 180px; height: 235px;
    background: radial-gradient(circle at 50% 60%, #b82727 0%, var(--stopwatch) 45%, #3a3a3a 72%, transparent 74%);
  }
  .credentials {
    position: absolute; top: 805px; width: 800px; text-align: center;
    font-size: 31px; font-weight: 500; line-height: 46px; letter-spacing: 1px;
  }
  .payments {
    position: absolute; top: 913px; left: 142px; width: 522px; height: 76px;
    display: flex; gap: 10px;
  }
  .pay-card {
    flex: 1; border-radius: 7px;
    background: var(--card-face);
    color: var(--card-ink);
    font-family: "Orbitron", sans-serif; font-weight: 700;
    display: flex; align-items: center; justify-content: center;
    font-size: 17px;
  }
  .pay-card.cash { background: linear-gradient(135deg, #a6b28c, var(--cash)); }
  .call-button {
    position: absolute; top: 1012px; left: 138px; width: 528px; height: 82px;
    border-radius: 10px;
    background: linear-gradient(180deg, var(--button-top) 0%, #1b63d6 50%, var(--button-bottom) 100%);
    border: 2px solid #0a2e78;
    color: var(--text);
    font-family: Arial, sans-serif; font-size: 34px;
    display: flex; align-items: center; justify-content: center;
    text-decoration: none;
  }
</style>
</head>
<body>
  <header class="site-header">
    <h1 class="brand-name">Breval Keyworks</h1>
    <p class="phone">0438210957</p>
  </header>

  <div class="keys" role="img" aria-label="Row of six car and house keys"></div>

  <p class="question">Locked out of your home or office?</p>
  <p class="offer-band">$150 gets you in easy!</p>

  <div class="service-badge" role="img" aria-label="Red stopwatch badge reading 24 hour service"></div>

  <div class="credentials">
    <p>ABN: 51824753296</p>
    <p>Master Licence: 407316582</p>
  </div>

  <div class="payments">
    <span class="pay-card">Brixalonte</span>
    <span class="pay-card">Orla</span>
    <span class="pay-card cash" role="img" aria-label="Cash banknote"></span>
    <span class="pay-card">Quidlo</span>
  </div>

  <a class="call-button" href="tel:0438210957">Click to Call</a>
</body>
</html>
```